Business Card for Marriage Commissioner

I am a marriage commissioner in the province of Alberta, meaning that I perform civil unions here. I have been trying to think of a unique design for my business card, something a bit different. A lot of "unique" designs seem to incorporate unique cuts or "some assembly required" or printed on plastic or meat. I would like my design to be a full colour card that is a typical business card size.

The information on the card should have:
Lon Varbeck
my occupation: Marriage Commissioner
my website: www.lonvarbeck.ca
my e-mail: lon@lonvarbeck.ca
my phone: 780-914-2086

I originally submitted a design to the printer that had a screen capture of a finduro search window, with my name and occupation in the text box. And underneath that, my phone number. Nothing else. They indicated they could not print this because it was a copyright violation.

One option on the design is I am a retired chemist-so a chemistry themed card would also be of interest, as long as it isn't a "Quiet Reagent" theme, as I have that on my other business cards already...

I would prefer a single sided card, but I am open to a double sided card if it is clever!

I would also prefer not to have pictures of male and female couples as in my position I will also marry same sex couples. Same thing for male/female symbols. Someone has submitted two graduated cylinders in love, which is very clever, and gets around this male/female type.

Thanks for your help and interest.

Target Market(s)

Young couples.

Industry/Entity Type

Plastic

Requirements
Nice to have
• chemistry ideas!
Should not have
• Male/female pictures, male/female symbols.
No QR codes.
No transparent designs, will go on paper stock.

```html
<!DOCTYPE html>
<html lang="en">
<head>
<meta charset="utf-8">
<title>Lon Varbeck – Marriage Commissioner business card</title>
<link rel="stylesheet" href="https://fonts.googleapis.com/css2?family=Pinyon+Script&family=Lobster&family=Open+Sans:wght@400;600&display=swap">
<style>
  :root {
    --stage: #2e2420;
    --frame: #6c6560;
    --tan-dark: #b3a27e;
    --tan: #c8b894;
    --cream: #e6dbc2;
    --cream-light: #efe6d2;
    --halo: #dccfac;
    --photo-green: #8fa66a;
    --photo-ivory: #f1ece4;
    --ink-blue: #1d4f8f;
    --ink-dark: #1f1f1f;
    --ink-grey: #6a6560;
    --rule: #7b7266;
    --ring-gold: #c9b58e;
    --ring-plum: #7d6474;
    --dove: #efe9dc;
  }
  * { box-sizing: border-box; margin: 0; padding: 0; }
  html, body {
    width: 1200px; height: 901px; overflow: hidden;
    background: var(--stage);
  }
  .card {
    position: absolute; left: 370px; top: 40px;
    width: 460px; height: 820px;
    background: var(--frame);
    padding: 16px;
  }
  .card__face {
    position: relative; width: 100%; height: 100%; overflow: hidden;
    background: linear-gradient(180deg, var(--tan-dark) 0%, var(--tan) 40%, var(--cream) 68%, var(--cream-light) 100%);
  }
  .halo {
    position: absolute; left: 110px; top: 10px;
    width: 320px; height: 320px; border-radius: 50%;
    background: var(--halo); opacity: .85;
  }
  .portrait {
    position: absolute; left: 120px; top: 40px;
    width: 300px; height: 300px; border-radius: 50%;
    background: radial-gradient(circle at 50% 45%, var(--photo-ivory) 0%, #d9d3c6 45%, var(--photo-green) 100%);
    box-shadow: 0 0 0 4px rgba(255,255,255,.7), 0 4px 12px rgba(0,0,0,.25);
  }
  .tick { position: absolute; background: var(--cream-light); opacity: .8; width: 2px; }
  .tick--a { left: 410px; top: 150px; height: 40px; }
  .tick--b { left: 405px; top: 320px; height: 30px; }
  .motto {
    position: absolute; left: 30px; top: 350px; width: 400px;
    font-family: "Pinyon Script", cursive; font-size: 48px;
    color: #fff; text-shadow: 1px 2px 2px rgba(40,30,20,.75);
    white-space: nowrap;
  }
  .dove {
    position: absolute; left: 30px; top: 415px;
    width: 190px; height: 70px; border-radius: 50%;
    background: radial-gradient(ellipse at center, var(--dove) 0%, rgba(239,233,220,0) 70%);
  }
  .rings {
    position: absolute; left: 316px; top: 478px;
    width: 100px; height: 72px; border-radius: 50%;
    background: radial-gradient(ellipse at center, var(--ring-gold) 0%, var(--ring-gold) 35%, var(--ring-plum) 65%, rgba(125,100,116,0) 72%);
  }
  .rule { position: absolute; height: 1px; background: var(--rule); }
  .rule--top { left: 40px; top: 472px; width: 270px; }
  .rule--bottom { left: 40px; top: 598px; width: 350px; }
  .name {
    position: absolute; left: 40px; top: 478px;
    font-family: "Lobster", cursive; font-size: 50px; font-weight: 400;
    line-height: 66px;
    color: var(--ink-blue); white-space: nowrap;
  }
  .occupation {
    position: absolute; left: 150px; top: 558px;
    font-family: "Open Sans", sans-serif; font-size: 22px; line-height: 30px;
    color: var(--ink-grey); white-space: nowrap;
  }
  .contacts {
    position: absolute; left: 34px; top: 612px; list-style: none;
    font-family: "Open Sans", sans-serif; font-size: 26px; color: var(--ink-dark);
  }
  .contacts li { display: flex; align-items: center; height: 42px; }
  .contacts svg { width: 26px; height: 26px; margin-right: 12px; flex: none; }
</style>
</head>
<body>
  <div class="card">
    <div class="card__face">
      <div class="halo"></div>
      <div class="portrait" role="img" aria-label="Round wedding portrait of a happy couple on a lawn"></div>
      <div class="tick tick--a"></div>
      <div class="tick tick--b"></div>

      <p class="motto">Love, Forgive, Grow</p>

      <div class="dove" role="img" aria-label="White dove in flight"></div>
      <div class="rings" role="img" aria-label="Pair of interlocked wedding rings"></div>

      <div class="rule rule--top"></div>
      <h1 class="name">Lon Varbeck</h1>
      <p class="occupation">Marriage Commissioner</p>
      <div class="rule rule--bottom"></div>

      <ul class="contacts">
        <li>
          <svg viewBox="0 0 26 26" aria-hidden="true"><circle cx="13" cy="13" r="13" fill="var(--ink-blue)"/><path d="M8.5 7.5c1-.9 2-.7 2.4.2l1 2c.3.7.1 1.3-.5 1.7l-.7.5c.6 1.4 1.7 2.6 3.1 3.3l.6-.7c.4-.6 1.1-.7 1.7-.4l2 1c.9.4 1 1.5.2 2.4-1 1.1-2.6 1.3-4.3.4-2.7-1.4-4.6-3.5-5.8-6.2-.7-1.6-.6-3.2.3-4.2z" fill="#fff"/></svg>
          780-914-2086
        </li>
        <li>
          <svg viewBox="0 0 26 26" aria-hidden="true"><circle cx="13" cy="13" r="13" fill="var(--ink-blue)"/><rect x="6.5" y="8.5" width="13" height="9" fill="none" stroke="#fff" stroke-width="1.6"/><path d="M6.5 8.5l6.5 5 6.5-5" fill="none" stroke="#fff" stroke-width="1.6"/></svg>
          www.lonvarbeck.ca
        </li>
        <li>
          <svg viewBox="0 0 26 26" aria-hidden="true"><circle cx="13" cy="13" r="13" fill="var(--ink-blue)"/><path d="M11 15l4-4M10 12.5l-1.5 1.5a2.5 2.5 0 0 0 3.5 3.5l1.5-1.5M16 13.5l1.5-1.5a2.5 2.5 0 0 0-3.5-3.5L12.5 10" fill="none" stroke="#fff" stroke-width="1.8" stroke-linecap="round"/></svg>
          lon@lonvarbeck.ca
        </li>
      </ul>
    </div>
  </div>
</body>
</html>
```